A Skycast Site needs designs

We need a website design for our new venture which is a Skycast website. This website should have the latest design trends.

Menu
Weather, Maps, Videos and Photos

The home page requirements are as follows:
- Search Bar
- Local Weather
- Weather forecast of major cities in the World
Favorite locations
- Space for ADs
- Email signup

Weather Details page
This page will be redirected from the home page when you click on any of the weather forecast section

We are open to all kinds of designs and ideas. Feel free to you colors which suite your design.

```html
<!DOCTYPE html>
<html lang="en">
<head>
<meta charset="utf-8">
<title>Skycast — Weather</title>
<link href="https://fonts.googleapis.com/css2?family=Roboto:wght@300;400;500;700&display=swap" rel="stylesheet">
<style>
:root{
  --page:#151a38;
  --white:#ffffff;
  --brand:#0f58a8;
  --brand-dark:#0b4b94;
  --brand-bright:#1161b6;
  --ad:#1f2649;
  --ad-text:#7d84a8;
  --ink:#222;
  --muted:#666;
  --tab:#e2e2e2;
  --sun:#f6c516;
  --card:rgba(30,22,30,.55);
  --map-tone:#dfe3df;
}
*{margin:0;padding:0;box-sizing:border-box}
html,body{width:1080px;height:1200px;overflow:hidden;background:var(--page);font-family:'Roboto',sans-serif}
.stage{position:absolute;left:0;top:0;width:1340px;height:1489px;transform:scale(.806);transform-origin:0 0;background:var(--page)}
.abs{position:absolute}
/* header */
.topbar{left:85px;top:0;width:1170px;height:81px;background:var(--white)}
.brand-block{left:85px;top:0;width:120px;height:113px;background:var(--brand);display:flex;align-items:center;justify-content:center;z-index:3}
.brand-name{color:var(--white);font-weight:500;font-size:20px}
.nav-item{top:0;height:81px;line-height:78px;font-size:15px;color:#333;letter-spacing:.2px}
.nav-item.active{background:var(--tab);padding:0 16px}
.unit{top:24px;font-size:13px;color:#444}
.unit.on{left:957px;width:28px;height:28px;line-height:28px;text-align:center;border-radius:50%;background:var(--tab)}
.signup{left:1072px;top:31px;font-size:14px;color:#444}
.login{left:1136px;top:22px;width:90px;height:34px;border:1.5px solid var(--brand);border-radius:17px;color:var(--brand);font-weight:500;font-size:14px;text-align:center;line-height:31px}
/* hero */
.hero-photo{left:85px;top:81px;width:1170px;height:550px;background:
 radial-gradient(ellipse at 60% 40%,rgba(255,120,40,.55),transparent 55%),
 linear-gradient(180deg,#2c3656 0%,#3d4566 30%,#7a3a2a 65%,#c9462a 85%,#e0623a 100%)}
.hero-side{left:982px;top:81px;width:273px;height:550px;background:rgba(20,14,22,.45)}
.now-temp{left:1080px;top:118px;font-size:82px;font-weight:300;color:var(--white)}
.tag{font-size:14px;color:var(--white);text-transform:uppercase}
.city-now{left:1026px;top:220px;font-size:21px;color:var(--white)}
.stat{left:1072px;font-size:14px;color:var(--white)}
.search{left:115px;top:342px;width:430px;height:48px;background:var(--white);padding-left:19px;line-height:48px;font-size:15px;color:#555}
.search-btn{left:545px;top:342px;width:116px;height:48px;background:var(--brand);color:var(--white);font-weight:700;font-size:15px;text-align:center;line-height:50px}
.next-title{left:116px;top:416px;font-size:18px;color:var(--white);font-weight:300}
.next-link{left:262px;top:420px;font-size:12px;color:var(--white);text-decoration:underline}
.fc-card{top:448px;height:153px;background:var(--card)}
.fc-label{top:473px;font-size:14px;color:var(--white)}
.fc-temp{top:492px;font-size:76px;font-weight:300;color:var(--white);line-height:1}
.fc-small{top:553px;font-size:11px;color:var(--white)}
/* ads */
.ad{background:var(--ad);color:var(--ad-text);font-size:16px;display:flex;align-items:center;justify-content:center}
/* map */
.map{left:85px;top:742px;width:580px;height:460px;background:var(--map-tone)}
.map-label{left:85px;top:742px;width:275px;height:61px;background:var(--white);line-height:61px;padding-left:29px;font-size:15px;color:#333}
.map-label span{color:var(--muted);margin-left:6px}
/* cities */
.city-card{top:742px;height:224px;overflow:hidden}
.city-name{font-size:14px;color:var(--white)}
.city-temp{font-size:60px;font-weight:300;color:var(--white);line-height:1}
.city-next{left:1195px;top:742px;width:61px;height:224px;background:var(--brand)}
/* favorites */
.fav{left:676px;top:978px;width:580px;height:224px;background:var(--white)}
.fav-title{left:737px;top:1004px;font-size:16px;font-weight:500;color:var(--ink)}
.fav-row{position:relative;height:28px;line-height:28px;font-size:16px;color:var(--ink);width:225px;padding-left:6px}
.fav-row b{position:absolute;right:8px;font-weight:700;font-size:15px}
.fav-row.hl{background:#ededed}
.fav-col-right .fav-row{font-size:17px}
/* footer */
.foot-nav{left:85px;top:1212px;width:1170px;height:44px;background:var(--brand-bright)}
.foot-link{top:1225px;font-size:15px;font-weight:700;color:var(--white)}
.foot-body{left:85px;top:1256px;width:1170px;height:147px;background:var(--brand)}
.foot-brand{left:127px;top:1315px;font-size:18px;font-weight:500;color:#5f92cf}
.copy{left:255px;top:1308px;font-size:14px;line-height:22px;color:var(--white)}
.social{top:1315px;width:22px;height:22px;border-radius:50%;background:var(--white)}
</style>
</head>
<body>
<div class="stage">
  <!-- header -->
  <div class="abs topbar"></div>
  <div class="abs brand-block"><span class="brand-name">Skycast</span></div>
  <div class="abs nav-item active" style="left:246px">WEATHER</div>
  <div class="abs nav-item" style="left:378px">MAPS</div>
  <div class="abs nav-item" style="left:468px">VIDEOS</div>
  <div class="abs nav-item" style="left:567px">PHOTOS</div>
  <div class="abs unit on">C°</div>
  <div class="abs unit" style="left:1001px;top:30px">F°</div>
  <div class="abs signup">Sign up</div>
  <div class="abs login">LOG IN</div>

  <!-- hero -->
  <div class="abs hero-photo" role="img" aria-label="Photo of a lit suspension bridge at dusk under a cloudy orange sky"></div>
  <div class="abs hero-side"></div>
  <svg class="abs" style="left:1026px;top:134px" width="46" height="40" viewBox="0 0 46 40" fill="none" stroke="#f6c516" stroke-width="3"><circle cx="30" cy="14" r="8"/><path d="M30 1v3M41 4l-2 2M44 14h-3"/><path d="M10 36h22a8 8 0 0 0 0-16 11 11 0 0 0-21 3 7 7 0 0 0-1 13z" fill="#2a1c22"/></svg>
  <div class="abs tag" style="left:1027px;top:184px">Clear</div>
  <div class="abs now-temp">26°</div>
  <div class="abs city-now">SAN FRANCISCO, CA</div>
  <svg class="abs" style="left:1030px;top:282px" width="18" height="18" viewBox="0 0 18 18" fill="none" stroke="#fff" stroke-width="2"><circle cx="9" cy="9" r="7.5"/><path d="M9 4v5h4"/></svg>
  <div class="abs stat" style="top:283px">11:02 am</div>
  <svg class="abs" style="left:1026px;top:332px" width="26" height="16" viewBox="0 0 26 16" fill="none" stroke="#fff" stroke-width="2"><path d="M1 5h16a3 3 0 1 0-3-3M1 10h21a3 3 0 1 1-3 3"/></svg>
  <div class="abs stat" style="top:331px">13 km/h</div>
  <svg class="abs" style="left:1033px;top:374px" width="12" height="22" viewBox="0 0 12 22" fill="none" stroke="#fff" stroke-width="2"><path d="M4 3a2 2 0 0 1 4 0v10a4 4 0 1 1-4 0z"/></svg>
  <div class="abs stat" style="top:379px">61%</div>
  <svg class="abs" style="left:1034px;top:450px" width="42" height="28" viewBox="0 0 42 28" fill="none" stroke="#f6c516" stroke-width="2.5"><path d="M12 22a9 9 0 0 1 18 0M4 26h34M21 4v4M7 10l3 3M35 10l-3 3M1 20h4M37 20h4M21 20v-7M17 16l4-4 4 4"/></svg>
  <div class="abs stat" style="left:1026px;top:491px">05:24 pm</div>
  <svg class="abs" style="left:1140px;top:450px" width="42" height="28" viewBox="0 0 42 28" fill="none" stroke="#f6c516" stroke-width="2.5"><path d="M12 22a9 9 0 0 1 18 0M4 26h34M21 4v4M7 10l3 3M35 10l-3 3M1 20h4M37 20h4M21 12v7M17 16l4 4 4-4"/></svg>
  <div class="abs stat" style="left:1131px;top:493px">04:30 am</div>

  <div class="abs search">Search City, index or airport</div>
  <div class="abs search-btn">SEARCH</div>
  <div class="abs next-title">NEXT 24 HOURS</div>
  <div class="abs next-link">See full information</div>

  <div class="abs fc-card" style="left:115px;width:230px"></div>
  <div class="abs fc-card" style="left:351px;width:241px"></div>
  <div class="abs fc-card" style="left:602px;width:233px"></div>
  <div class="abs fc-card" style="left:845px;width:36px"></div>
  <svg class="abs" style="left:856px;top:516px" width="14" height="18" viewBox="0 0 14 18" fill="none" stroke="#fff" stroke-width="2.5"><path d="M3 2l7 7-7 7"/></svg>

  <div class="abs fc-label" style="left:155px">TODAY</div>
  <svg class="abs" style="left:154px;top:506px" width="42" height="36" viewBox="0 0 46 40" fill="none" stroke="#f6c516" stroke-width="3"><circle cx="30" cy="14" r="8"/><path d="M30 1v3M41 4l-2 2M44 14h-3"/><path d="M10 36h22a8 8 0 0 0 0-16 11 11 0 0 0-21 3 7 7 0 0 0-1 13z" fill="#3a2628"/></svg>
  <div class="abs fc-small" style="left:158px">CLEAR</div>
  <div class="abs fc-temp" style="left:203px">26°</div>

  <div class="abs fc-label" style="left:411px">TOMORROW</div>
  <svg class="abs" style="left:408px;top:506px" width="44" height="44" viewBox="0 0 44 44" fill="none" stroke="#f6c516" stroke-width="3"><circle cx="22" cy="22" r="8"/><path d="M22 2v6M22 36v6M2 22h6M36 22h6M8 8l4 4M32 32l4 4M36 8l-4 4M8 36l4-4"/></svg>
  <div class="abs fc-small" style="left:410px">SUNNY</div>
  <div class="abs fc-temp" style="left:458px">18°</div>

  <div class="abs fc-label" style="left:642px">TOMORROW NIGHT</div>
  <svg class="abs" style="left:640px;top:506px" width="42" height="40" viewBox="0 0 42 40" fill="none" stroke="#f6c516" stroke-width="3"><path d="M10 26h22a8 8 0 0 0 0-16 11 11 0 0 0-21 3 7 7 0 0 0-1 13z"/><path d="M14 30v4M21 30v6M28 30v4"/></svg>
  <div class="abs fc-small" style="left:643px">RAINY</div>
  <div class="abs fc-temp" style="left:690px">8°</div>

  <!-- ads -->
  <div class="abs ad" style="left:85px;top:641px;width:580px;height:91px">YOUR ADS BANNER GOES HERE</div>
  <div class="abs ad" style="left:675px;top:641px;width:580px;height:91px">YOUR ADS BANNER GOES HERE</div>

  <!-- map -->
  <div class="abs map" role="img" aria-label="Cloud coverage map of the San Francisco Bay Area"></div>
  <div class="abs map-label">CLOUDS<span>SAN FRANCISCO, CA</span></div>

  <!-- cities -->
  <div class="abs city-card" style="left:676px;width:224px;background:linear-gradient(180deg,#3a7fc7 0%,#2e4f7a 45%,#1a2536 100%)" role="img" aria-label="Photo of Paris at dusk with the lit iron tower"></div>
  <div class="abs city-name" style="left:694px;top:869px">Paris, France</div>
  <svg class="abs" style="left:695px;top:893px" width="36" height="34" viewBox="0 0 42 40" fill="none" stroke="#f6c516" stroke-width="3"><path d="M10 26h22a8 8 0 0 0 0-16 11 11 0 0 0-21 3 7 7 0 0 0-1 13z"/><path d="M14 30v4M21 30v6M28 30v4"/></svg>
  <div class="abs" style="left:698px;top:935px;font-size:9px;color:#fff">RAINY</div>
  <div class="abs city-temp" style="left:736px;top:896px">12°</div>

  <div class="abs city-card" style="left:910px;width:224px;background:linear-gradient(180deg,#8fb6d8 0%,#6c7b82 50%,#3a3630 100%)" role="img" aria-label="Photo of London with the clock tower and street lamps"></div>
  <div class="abs city-name" style="left:931px;top:869px">London, UK</div>
  <svg class="abs" style="left:932px;top:895px" width="34" height="34" viewBox="0 0 44 44" fill="none" stroke="#f6c516" stroke-width="3"><circle cx="22" cy="22" r="8"/><path d="M22 2v6M22 36v6M2 22h6M36 22h6M8 8l4 4M32 32l4 4M36 8l-4 4M8 36l4-4"/></svg>
  <div class="abs" style="left:931px;top:935px;font-size:9px;color:#fff">SUNNY</div>
  <div class="abs city-temp" style="left:972px;top:896px">20°</div>

  <div class="abs city-card" style="left:1144px;width:51px;background:linear-gradient(180deg,#d8a070 0%,#a0623c 60%,#6a3a22 100%)" role="img" aria-label="Photo of an ancient Roman amphitheatre"></div>
  <div class="abs city-next"></div>
  <svg class="abs" style="left:1215px;top:841px" width="18" height="28" viewBox="0 0 18 28" fill="none" stroke="#fff" stroke-width="3.5"><path d="M3 3l11 11-11 11"/></svg>

  <!-- favorites -->
  <div class="abs fav"></div>
  <svg class="abs" style="left:705px;top:1004px" width="20" height="19" viewBox="0 0 24 23"><path d="M12 0l3.5 7.6 8.3.9-6.2 5.6 1.8 8.2L12 18l-7.4 4.3 1.8-8.2L.2 8.5l8.3-.9z" fill="#f6c516"/></svg>
  <div class="abs fav-title">FAVORITE PLACES</div>
  <div class="abs" style="left:703px;top:1042px">
    <div class="fav-row">New York<b>30°</b></div>
    <div class="fav-row hl">Los Angeles<b>21°</b></div>
    <div class="fav-row">Chicago<b>16°</b></div>
    <div class="fav-row">Dallas<b>32°</b></div>
    <div class="fav-row">Houston<b>9°</b></div>
  </div>
  <div class="abs fav-col-right" style="left:983px;top:1042px">
    <div class="fav-row">Washington<b>30°</b></div>
    <div class="fav-row">Philadelphia<b>21°</b></div>
    <div class="fav-row">Miami<b>16°</b></div>
    <div class="fav-row">Atlanta<b>32°</b></div>
    <div class="fav-row">Boston<b>9°</b></div>
  </div>

  <!-- footer -->
  <div class="abs foot-nav"></div>
  <div class="abs foot-link" style="left:127px">WEATHER</div>
  <div class="abs foot-link" style="left:243px">MAPS</div>
  <div class="abs foot-link" style="left:333px">VIDEOS</div>
  <div class="abs foot-link" style="left:432px">PHOTOS</div>
  <div class="abs foot-body"></div>
  <div class="abs foot-brand">Skycast</div>
  <div class="abs copy">©2017 Skycast, Inc.<br>All rights reserved.</div>
  <div class="abs ad" style="left:499px;top:1281px;width:383px;height:96px;background:var(--brand-dark);color:#7ea4d4">YOUR ADS BANNER GOES HERE</div>
  <div class="abs social" style="left:941px" aria-label="Social link"></div>
  <div class="abs social" style="left:988px" aria-label="Social link"></div>
  <div class="abs social" style="left:1035px" aria-label="Social link"></div>
  <div class="abs social" style="left:1082px" aria-label="Social link"></div>
  <div class="abs social" style="left:1129px" aria-label="Social link"></div>
  <div class="abs social" style="left:1176px" aria-label="Social link"></div>
</div>
</body>
</html>
```